Nutrition business needs logo & business card design

We need a business card & logo design for a new company based in Toronto, Ontario Canada called Verdel Wellcraft.

We provide nutrition service using metrics as guide to manage client's progress. Our service creates individualized nutrition and lifestyle strategies that focuses on improving Performance, Longevity and Weight Loss. I would like to see designs that use the color of green, gray, blue and white.

The final design should:

--convey a feeling of connectedness with positive transformation.

-- communicate the idea of awareness with guided effort that yields personal independence for a better and more productive life

Target Market(s)

Professionals who work in the IT/Computer/Engineering/Banking industry specifically Directors, Managers, CEO's.

Industry/Entity Type

Health And Wellness

Contact Information for Business Card

Domric Hale, Owner
email: DHALE@verdelwellcraft.example
tel: - 555-274-9038

Logo Text

better health through analytics or measure to manage

Font styles to use
Other font styles liked:
• Garamound

Colors
ffffff
abd037
85acd3
757575
34a7d7

Requirements
Must have
• Good contrast and decent size font - ease of readability, aesthetically nice colors
Nice to have
• image of chart or graph that conveys measurement or analytics
Should not have
• Borders, images of food,

```html
<!DOCTYPE html>
<html lang="en">
<head>
<meta charset="utf-8">
<title>Verdel Wellcraft — Business Cards</title>
<link rel="stylesheet" href="https://fonts.googleapis.com/css2?family=Open+Sans:wght@400;600&family=Oswald:wght@600&display=swap">
<style>
  :root {
    --backdrop: #2e2927;
    --card: #111111;
    --card-edge: #1c1c1c;
    --green: #abd037;
    --green-deep: #5fb246;
    --blue: #34a7d7;
    --blue-soft: #85acd3;
    --gray: #757575;
    --white: #ffffff;
    --text-soft: #d6d6d6;
  }
  * { box-sizing: border-box; margin: 0; padding: 0; }
  html, body { width: 1200px; height: 900px; overflow: hidden; }
  body {
    background: var(--backdrop);
    position: relative;
    font-family: "Open Sans", Arial, sans-serif;
  }
  .card {
    position: absolute;
    top: 300px;
    width: 525px;
    height: 300px;
    background: var(--card);
    border: 1px solid var(--card-edge);
    box-shadow: 0 10px 30px rgba(0,0,0,.45);
  }
  .card--contact { left: 45px; }
  .card--front { left: 630px; }

  /* contact side */
  .brand-block {
    position: absolute;
    left: 0; top: 0;
    width: 250px; height: 300px;
    display: flex; align-items: center; justify-content: center; gap: 10px;
  }
  .brand-dot {
    flex: none;
    width: 16px; height: 16px; border-radius: 50%;
    background: var(--blue);
  }
  .brand-name {
    font-family: "Oswald", Impact, sans-serif;
    font-weight: 600;
    font-size: 26px;
    color: var(--green);
    letter-spacing: .3px;
    white-space: nowrap;
  }
  .divider {
    position: absolute;
    left: 250px; top: 40px;
    width: 1px; height: 220px;
    background: linear-gradient(to bottom, transparent, var(--gray) 25%, var(--gray) 75%, transparent);
  }
  .details {
    position: absolute;
    left: 272px; top: 62px;
    color: var(--white);
    font-size: 13px;
    line-height: 1.45;
  }
  .person-name {
    color: var(--green);
    font-weight: 600;
    font-size: 16px;
    line-height: 1.2;
  }
  .person-title { color: var(--blue-soft); margin-bottom: 14px; }
  .address { color: var(--text-soft); margin-bottom: 14px; }
  .contact-list { list-style: none; }
  .contact-list li { display: flex; align-items: center; gap: 8px; }
  .contact-icon { width: 11px; height: 11px; flex: none; fill: var(--blue); }

  /* front side */
  .front-brand {
    position: absolute; inset: 0;
    display: flex; align-items: center; justify-content: center; gap: 14px;
  }
  .front-brand .brand-dot { width: 22px; height: 22px; }
  .front-brand .brand-name { font-size: 42px; }
</style>
</head>
<body>

<section class="card card--contact" aria-label="Business card, contact side">
  <div class="brand-block">
    <span class="brand-dot"></span>
    <span class="brand-name">Verdel Wellcraft</span>
  </div>
  <div class="divider"></div>
  <div class="details">
    <p class="person-name">Domric Hale</p>
    <p class="person-title">Owner</p>
    <p class="address">88 Harbour Lane,<br>Toronto, ON M5J 2N8.</p>
    <ul class="contact-list">
      <li>
        <svg class="contact-icon" viewBox="0 0 24 24" aria-hidden="true"><path d="M6.6 10.8a15.2 15.2 0 0 0 6.6 6.6l2.2-2.2a1 1 0 0 1 1-.25 11.4 11.4 0 0 0 3.6.57 1 1 0 0 1 1 1V20a1 1 0 0 1-1 1A17 17 0 0 1 3 4a1 1 0 0 1 1-1h3.5a1 1 0 0 1 1 1c0 1.25.2 2.45.57 3.6a1 1 0 0 1-.25 1z"/></svg>
        <span>555-274-9038</span>
      </li>
      <li>
        <svg class="contact-icon" viewBox="0 0 24 24" aria-hidden="true"><path d="M2 5h20v2l-10 7L2 7z"/><path d="M2 9l10 7 10-7v10H2z"/></svg>
        <span>DHALE@verdelwellcraft.example</span>
      </li>
      <li>
        <svg class="contact-icon" viewBox="0 0 24 24" aria-hidden="true"><circle cx="12" cy="12" r="10"/></svg>
        <span>www.verdelwellcraft.example</span>
      </li>
    </ul>
  </div>
</section>

<section class="card card--front" aria-label="Business card, brand side">
  <div class="front-brand">
    <span class="brand-dot"></span>
    <span class="brand-name">Verdel Wellcraft</span>
  </div>
</section>

</body>
</html>
```